Refreshed PPT Presentation for US based firms

There are basically 4 types of slides in this presentation:
* Roadmap (Title, Agenda, Billboards)
* Teaching (Content, Examples)
* Samples (Real life samples)
* Polls (Placeholders for interactive polls)
We want new templates for each of these types of templates with coordinated graphics, images, icons and fonts.

```html
<!DOCTYPE html>
<html lang="en">
<head>
<meta charset="utf-8">
<title>Advice and Counsel Through Email – Slide Templates</title>
<link href="https://fonts.googleapis.com/css2?family=Mulish:wght@400;600;700;800;900&display=swap" rel="stylesheet">
<style>
:root{
  --stage:#6e6e70;
  --paper:#ffffff;
  --ink:#1f2633;
  --muted:#4b5260;
  --accent:#f47b20;
  --rule:#e2e2e2;
  --panel:#f1f1f1;
  --photo-warm-a:#c9a88a;
  --photo-warm-b:#5b4a3e;
  --photo-cool-a:#b8c1c7;
  --photo-cool-b:#4a5560;
}
*{box-sizing:border-box;margin:0;padding:0}
html,body{width:1200px;height:3912px;overflow:hidden}
body{background:var(--stage);font-family:"Mulish",sans-serif;color:var(--ink)}
.deck{position:relative;width:1200px;height:3912px}
.slide{position:absolute;left:104px;width:992px;height:580px;background:var(--paper);overflow:hidden}
.slide-header{position:absolute;left:0;top:0;width:100%;height:40px;border-bottom:1px solid var(--rule);padding:13px 18px;font-size:15px;font-weight:800}
.photo{position:absolute}
.accent-rule{width:44px;height:3px;background:var(--accent);margin-top:12px}
.bullets{list-style:none}
.bullets li{position:relative;padding-left:22px;font-size:14px;font-weight:600;color:var(--muted);margin-bottom:14px;line-height:1.35}
.bullets li::before{content:"";position:absolute;left:2px;top:5px;width:8px;height:8px;background:var(--accent);transform:rotate(45deg)}

/* Title */
.s-title{top:40px}
.s-title .photo{left:0;top:0;width:640px;height:580px;background:linear-gradient(110deg,var(--photo-warm-b) 0%,var(--photo-warm-a) 45%,#e8e2da 80%,#ffffff 100%)}
.s-title .brand{position:absolute;right:28px;top:22px;font-size:17px;font-weight:800}
.s-title h1{position:absolute;left:688px;top:218px;font-size:38px;font-weight:900;line-height:1.08;text-transform:uppercase}
.s-title .byline{position:absolute;left:688px;top:392px;font-size:9px;font-weight:800;text-transform:uppercase;letter-spacing:.3px}
.s-title .link{position:absolute;left:688px;bottom:24px;font-size:11px;color:var(--muted)}

/* Agenda */
.s-agenda{top:670px}
.s-agenda .photo{left:0;top:40px;width:520px;height:500px;background:linear-gradient(135deg,var(--photo-warm-b),var(--photo-warm-a) 55%,#8a8078)}
.s-agenda .content{position:absolute;left:588px;top:128px;width:380px}
.s-agenda h2{font-size:40px;font-weight:800}
.s-agenda .agenda-list{list-style:none;margin-top:26px}
.s-agenda .agenda-list>li{border-bottom:1px solid var(--rule);padding:9px 0 9px 18px;font-size:14px;font-weight:600;position:relative}
.s-agenda .agenda-list>li::before{content:"";position:absolute;left:2px;top:15px;width:7px;height:7px;background:var(--accent)}
.s-agenda .sub{list-style:none}
.s-agenda .sub li{border-bottom:1px solid var(--rule);padding:8px 0 8px 40px;font-size:12px;color:var(--muted);position:relative}
.s-agenda .sub li::before{content:"";position:absolute;left:24px;top:13px;width:6px;height:6px;background:var(--accent)}

/* Four stages */
.s-stages{top:1300px}
.s-stages h2{position:absolute;top:96px;width:100%;text-align:center;font-size:23px;font-weight:900}
.s-stages .accent-rule{position:absolute;left:474px;top:132px;margin:0}
.s-stages .stages{position:absolute;top:200px;left:40px;right:40px;display:flex;justify-content:space-around}
.stage{width:190px;text-align:center}
.stage .photo{position:static;width:176px;height:176px;border-radius:50%;margin:0 auto}
.stage p{margin-top:38px;font-size:13px;color:var(--muted);line-height:1.4}

/* Clarify */
.s-clarify{top:1930px}
.s-clarify .photo{left:0;top:40px;width:412px;height:540px;background:linear-gradient(120deg,var(--photo-cool-b),var(--photo-cool-a) 60%,#dcd8d2)}
.s-clarify .content{position:absolute;left:508px;top:86px;width:440px}
.s-clarify h2{font-size:28px;font-weight:900;line-height:1.1;text-transform:uppercase;margin-bottom:28px}
.s-clarify .scope{margin-top:28px;background:var(--panel);border:1px solid var(--rule);padding:26px 24px 14px}
.s-clarify .scope li{font-size:12.5px}

/* Audience billboard */
.s-audience{top:2560px}
.s-audience .photo{left:0;top:40px;width:992px;height:540px;background:linear-gradient(90deg,#8c5a45,#b8a07c 40%,#6e7b83 70%,#cfd3c9)}
.s-audience h2{position:absolute;top:300px;width:100%;text-align:center;font-size:40px;font-weight:900;color:#fff;text-transform:uppercase;letter-spacing:.5px}

/* Three skills */
.s-skills{top:3190px}
.s-skills .photo{right:0;top:40px;width:470px;height:540px;background:radial-gradient(ellipse at 60% 50%,#7e8a96 0%,#b6bcc2 45%,#ffffff 78%)}
.s-skills h2{position:absolute;left:54px;top:126px;font-size:25px;font-weight:900}
.s-skills .accent-rule{position:absolute;left:54px;top:160px;margin:0}
.s-skills .skills{position:absolute;left:54px;top:196px;list-style:none}
.skill{display:flex;align-items:center;gap:18px;width:346px;height:84px;background:var(--panel);padding:0 18px;margin-bottom:14px}
.skill svg{flex:none}
.skill span{font-size:13px;font-weight:600;line-height:1.4}
</style>
</head>
<body>
<main class="deck">

  <section class="slide s-title">
    <div class="photo" role="img" aria-label="Two colleagues in conversation in a bright office"></div>
    <div class="brand">Advice and Counsel</div>
    <h1>Advice<br>and Counsel<br>Through<br>Email</h1>
    <p class="byline">Dana Whitfield for Northbeam Law P.C.</p>
    <p class="link">Go to www.pollbridge.com/dwhitfield488</p>
  </section>

  <section class="slide s-agenda">
    <div class="slide-header">Advice and Counsel</div>
    <div class="photo" role="img" aria-label="Smiling professional at a meeting table"></div>
    <div class="content">
      <h2>AGENDA</h2>
      <div class="accent-rule"></div>
      <ul class="agenda-list">
        <li>Preparation and process</li>
        <li>Audience and purpose</li>
        <li>Characteristics of a quality response
          <ul class="sub">
            <li>Quick</li>
            <li>Clear</li>
            <li>Concise</li>
          </ul>
        </li>
      </ul>
    </div>
  </section>

  <section class="slide s-stages">
    <div class="slide-header">Advice and Counsel</div>
    <h2>FOUR STAGES OF THE WRITING PROCESS</h2>
    <div class="accent-rule"></div>
    <div class="stages">
      <div class="stage">
        <div class="photo" role="img" aria-label="Glowing light bulb on a dark background" style="background:radial-gradient(circle,#d9c8a0,#2b2f38 70%)"></div>
        <p>Madman, the creative force who generates the ideas</p>
      </div>
      <div class="stage">
        <div class="photo" role="img" aria-label="Architect's plans and drawing tools" style="background:radial-gradient(circle,#9aa3ad,#4a525c 75%)"></div>
        <p>Architect, the planner who builds the structure for the document</p>
      </div>
      <div class="stage">
        <div class="photo" role="img" aria-label="Carpenter's hands shaping wood" style="background:radial-gradient(circle,#c9a06c,#5a4128 75%)"></div>
        <p>Carpenter, the craftsman who writes a draft</p>
      </div>
      <div class="stage">
        <div class="photo" role="img" aria-label="Pen marking up a printed document" style="background:radial-gradient(circle,#e0b45a,#2c3e78 75%)"></div>
        <p>Judge, the reviewer who edits the draft</p>
      </div>
    </div>
  </section>

  <section class="slide s-clarify">
    <div class="slide-header">Advice and Counsel</div>
    <div class="photo" role="img" aria-label="Professional woman listening thoughtfully in a meeting"></div>
    <div class="content">
      <h2>Clarify the question<br>and the time</h2>
      <ul class="bullets">
        <li>Sometimes a little clarity is required</li>
        <li>Seek clarity in, again, a phone call or a short email</li>
        <li>Then confirm the scope of the inquiry in an email</li>
      </ul>
      <div class="scope">
        <ul class="bullets">
          <li>In scope: Address ability to restrict marijuana use in six states</li>
          <li>Out of scope: consequences of past practices in compliance department</li>
          <li>Timing</li>
        </ul>
      </div>
    </div>
  </section>

  <section class="slide s-audience">
    <div class="slide-header">Advice and Counsel</div>
    <div class="photo" role="img" aria-label="Team discussing notes at a whiteboard"></div>
    <h2>Nature of Audience</h2>
  </section>

  <section class="slide s-skills">
    <div class="slide-header">Advice and Counsel</div>
    <div class="photo" role="img" aria-label="Two colleagues working together at a laptop"></div>
    <h2>THREE SKILLS INVOLVED</h2>
    <div class="accent-rule"></div>
    <ul class="skills">
      <li class="skill">
        <svg width="44" height="44" viewBox="0 0 44 44"><circle cx="22" cy="22" r="22" fill="var(--accent)"/><circle cx="20" cy="20" r="7" fill="none" stroke="#fff" stroke-width="2.5"/><line x1="25" y1="25" x2="31" y2="31" stroke="#fff" stroke-width="3" stroke-linecap="round"/></svg>
        <span>Identifying a sentence that can be improved</span>
      </li>
      <li class="skill">
        <svg width="44" height="44" viewBox="0 0 44 44"><circle cx="22" cy="22" r="22" fill="var(--accent)"/><circle cx="22" cy="20" r="8" fill="#fff"/><rect x="18" y="28" width="8" height="5" fill="#fff"/></svg>
        <span>Identifying the problem</span>
      </li>
      <li class="skill">
        <svg width="44" height="44" viewBox="0 0 44 44"><circle cx="22" cy="22" r="22" fill="var(--accent)"/><rect x="14" y="11" width="16" height="22" fill="#fff"/><line x1="17" y1="17" x2="27" y2="17" stroke="var(--accent)" stroke-width="1.5"/><line x1="17" y1="21" x2="27" y2="21" stroke="var(--accent)" stroke-width="1.5"/><line x1="17" y1="25" x2="24" y2="25" stroke="var(--accent)" stroke-width="1.5"/></svg>
        <span>Revising the sentence</span>
      </li>
    </ul>
  </section>

</main>
</body>
</html>
```